Website Design For Kembo Hub Project

www.kembohub.com.au

As the name suggests i would like to have a design for this website... the website is nothing to do with night life or parties, but it is do everything to do with being online all the time, being available 24/7.

all information needed regarding anything to do with this City and its businesses. so, Basically This will be an online business directory for local businesses. What i am looking for is a website that can display Business listings in a pleasant, lively, friendly, attitude that reflects the towns people, this city boasts with a largest inland city in Australia, and a local university to match, it has its own airport, malls, markets and supermarkets. This website directory/each business layout will be very similar to the ones on www.sorrelby-web.com.au.

Wagga Wagga has a community of numerous backgrounds, cutlures, creeds and beliefs and religions to be a thriving one.

Therefore, i want the website to reflect its green hills and flowing rivers. The is a advertising point.

An online venue for the local and surrounding bussinesses to be found with a minimum amount of clicks and hassles. Essentially it is a business directory, but not just any directory you see online. I do not want it to look like the amber lists or pale lists. this website directory is specific to one location and its bussinesses are particular to that area. I want the website to almost have an emotion for that City, not just an army of black and white ants marching across the page.

Yours colours are you own imagination as long as it is visible and readable by majority of people; its colours are pleasant and not offensive to the eyes: i.e: not too bright, not too dark and depressing.

"kembohub" is to be included in your website design.
Updates

Reason: The deadline has been extended as there are few nice concepts however they need to be a bit more clean in its layout, the color choices are not quite right, as well as the banners need to look more presentable. Thanks

Target Market(s)

The Target Market is Small to Medum Businesses to List their business online and Gen Y and Mums & dads looking for services in the city of Wagga Wagga

Industry/Entity Type

Business Directory

Requirements
Must have
• Search Bar
Social Media Widgets (PalNest, Chirpo, Drift across)
Categories
Sliding Banners
Each Major Category Should have an image or a nice Icon representing the category

```html
<!DOCTYPE html>
<html lang="en">
<head>
<meta charset="utf-8">
<title>Kembo Hub – Local Business Directory</title>
<link href="https://fonts.googleapis.com/css2?family=Arimo:wght@400;700&family=Oswald:wght@600&display=swap" rel="stylesheet">
<style>
:root{
  --maroon:#8e0f3c;
  --maroon-dark:#6d0a2d;
  --panel:#e4eaf3;
  --panel-border:#cdd6e3;
  --slate-top:#6b6f82;
  --slate-bottom:#3a3e50;
  --text:#222;
  --page:#ffffff;
  --footer:#ececec;
}
*{margin:0;padding:0;box-sizing:border-box}
html,body{width:847px;height:1200px;overflow:hidden}
body{position:relative;font-family:"Arimo",Arial,sans-serif;color:var(--text);background:#fff}
.abs{position:absolute}
.top-band{left:0;top:0;width:847px;height:106px;background:linear-gradient(#373d4b,#2a2f3b)}
.footer-band{left:0;top:1052px;width:847px;height:148px;background:var(--footer)}
.page{left:32px;top:20px;width:790px;height:1061px;background:var(--page);border-radius:4px;box-shadow:0 1px 6px rgba(0,0,0,.35)}

.logo{left:48px;top:52px;display:flex;align-items:center;gap:7px}
.logo-mark{width:18px;height:18px;background:var(--maroon)}
.logo-name{font-weight:700;font-size:15px;color:var(--maroon)}

.search{left:600px;top:46px;width:210px;height:28px;border:1px solid #c9ccd2;border-radius:4px;background:linear-gradient(#fff,#f0f1f3)}
.search span{position:absolute;left:17px;top:8px;font-size:9px;font-style:italic;color:#777}
.search-btn{position:absolute;left:186px;top:4px;width:19px;height:18px;border-radius:3px;background:linear-gradient(#4f7fb3,#2a5486)}
.hint{right:35px;top:95px;font-size:9px;color:#111}

.slider{left:41px;top:116px;width:772px;height:224px;border-radius:5px;background:radial-gradient(ellipse at 65% 45%,#fbfbfc,#dfe1e5 90%)}
.slider-photo{left:60px;top:150px;width:300px;height:190px;background:linear-gradient(#d8dbe0,#b9b4ae);border-radius:4px 4px 0 0}
.slide-title{left:402px;top:201px;font-size:19px;font-weight:400;color:var(--maroon)}
.slide-text{left:402px;top:236px;font-size:12px;line-height:19px;color:#9a9ea4}
.dot{top:307px;width:13px;height:13px;border-radius:50%;background:#7d7f84}
.dot.on{background:var(--maroon)}

.nav{left:41px;top:344px;width:772px;height:38px;border-radius:4px;background:linear-gradient(#a5194b,var(--maroon) 50%,var(--maroon-dark))}
.nav a{position:absolute;top:11px;font-size:13px;color:#fff;text-decoration:none}
.nav .sep{position:absolute;top:0;width:1px;height:38px;background:#6a0a2c;box-shadow:1px 0 0 #b43261}
.nav .home{left:19px;top:0;width:71px;height:38px;background:linear-gradient(#fff,#d4d9e2);color:#111;text-align:center;padding-top:11px}

.panel{background:var(--panel);border:1px solid var(--panel-border);border-radius:5px}
.ribbon{height:32px;color:#fff;font-size:14px;padding:8px 0 0 28px;background:linear-gradient(#5a5e70,#3d4152)}
.ribbon.light{background:linear-gradient(#f2f5f9,#dde3ec);color:#111;font-size:13px;padding:8px 0 0 19px}
.ribbon.dark-sm{font-size:13px;padding:8px 0 0 24px}
.ribbon::before{content:"";position:absolute;left:0;top:32px;border-top:8px solid #22252f;border-left:8px solid transparent}
.ribbon.light::before{border-top-color:#9aa2b0}

.cat-list{list-style:none;font-size:10.5px}
.cat-list li{position:absolute;left:0;white-space:nowrap}
.cat-list li::before{content:">>";font-size:7px;margin-right:8px;color:#333}

.biz-title{left:241px;top:414px;font-size:14px;font-weight:400;color:var(--maroon)}
.biz-col{list-style:none;font-size:9.5px}
.biz-col li{height:19.5px;white-space:nowrap}
.biz-col li::before{content:">";font-size:8px;margin-right:4px}
.biz-rule{left:243px;top:650px;width:366px;border-top:1px dotted #888}

.news p{position:absolute;left:13px;width:160px;font-size:10px;line-height:15px}
.news p::before{content:">>";font-size:7px;margin-right:8px}

.alpha{left:40px;top:669px;width:772px;height:38px;border:1px solid #b9bcc2;border-radius:4px;background:linear-gradient(#fff,#eceef1)}
.alpha span{position:absolute;top:13px;font-size:11.5px;color:#111}

.box-dark{background:linear-gradient(var(--slate-top),var(--slate-bottom));border:2px solid #c9ced8;border-radius:5px}
.box-light{background:var(--panel);border:1px solid var(--panel-border);border-radius:5px}
.reloc a{position:absolute;left:27px;font-size:13.5px;color:#fff;text-decoration:none}
.reloc a::before{content:">>";font-size:8px;margin-right:6px}
.field{width:141px;height:25px;border:1px solid #a9adb5;border-radius:5px;background:linear-gradient(#fff,#e6e8ec);font-size:10.5px;padding:6px 0 0 11px}
.btn{font-size:11px;border-radius:3px;text-align:center;padding-top:5px;height:23px}
.btn.dark{background:linear-gradient(#5d6174,#373a4b);color:#fff;border:1px solid #2a2c38}
.btn.light{background:linear-gradient(#f2f3f5,#cfd3da);color:#111;border:1px solid #8f939d}

.avatar{left:662px;top:785px;width:38px;height:37px;border:1px solid #aaa;background:linear-gradient(#e6e6e6,#c2c2c2)}
.testi-name{left:711px;top:790px;font-size:10px}
.testi-date{left:711px;top:806px;font-size:8px;font-weight:700}
.testi-text{left:655px;top:834px;width:155px;font-size:10px;line-height:15px;color:#333}
.testi-text::before{content:">>";font-size:7px;margin-right:6px}

.ad{left:115px;top:928px;width:616px;height:76px;overflow:hidden;background:linear-gradient(#23a150,#177a39)}
.ad-head{position:absolute;left:5px;top:11px;width:370px;font-family:"Oswald","Arial Narrow",sans-serif;font-weight:600;font-size:34px;line-height:50px;color:#fff;white-space:nowrap;letter-spacing:-.3px}
.ad-ball{position:absolute;left:378px;top:2px;width:72px;height:72px;border-radius:50%;background:radial-gradient(circle at 40% 35%,#eeeeee,#8d8d8d)}
.ad-brand{position:absolute;left:465px;top:21px;display:flex;align-items:center;gap:6px;color:#fff;font-size:20px;white-space:nowrap}
.ad-brand i{display:block;width:24px;height:24px;border-radius:50%;background:#f3c316}
.ad-url{position:absolute;left:467px;top:52px;font-size:8px;color:#fff;white-space:nowrap}

.social{top:1110px;width:20px;height:20px;border-radius:2px}
.footer-links{left:0;width:847px;top:1114px;text-align:center;font-size:9.5px}
.copy{left:0;width:847px;top:1146px;text-align:center;font-size:9px}
.roo{left:690px;top:1056px;width:128px;height:128px;border-radius:40% 40% 10% 10%;background:radial-gradient(ellipse at 45% 55%,#a88466,#e4dcd3 70%,transparent 72%)}
</style>
</head>
<body>
<div class="abs top-band"></div>
<div class="abs footer-band"></div>
<div class="abs page"></div>

<header>
  <div class="abs logo"><span class="logo-mark"></span><span class="logo-name">Kembo Hub</span></div>
  <div class="abs search"><span>Search</span>
    <div class="search-btn"><svg width="19" height="18" viewBox="0 0 19 18"><circle cx="8" cy="7.5" r="3.5" fill="none" stroke="#fff" stroke-width="1.6"/><line x1="10.5" y1="10" x2="14" y2="13.5" stroke="#fff" stroke-width="2"/></svg></div>
  </div>
  <p class="abs hint">Please click on a category and/or business name for more detailed information.</p>
</header>

<section class="abs slider"></section>
<div class="abs slider-photo" role="img" aria-label="Group of smiling local business people"></div>
<h1 class="abs slide-title">Lorem ipsum dolor sit amet</h1>
<p class="abs slide-text">Lorem ipsum dolor sit amet, consectetuer adipiscing elit.<br>Nam nibh. Nunc varius facilisis eros. Sed erat.</p>
<span class="abs dot on" style="left:710px"></span><span class="abs dot" style="left:735px"></span><span class="abs dot" style="left:760px"></span><span class="abs dot" style="left:785px"></span>

<nav class="abs nav">
  <a class="home" href="#">Home</a>
  <span class="sep" style="left:90px"></span>
  <a href="#" style="left:109px">About Kembo Hub</a>
  <span class="sep" style="left:228px"></span>
  <a href="#" style="left:249px">Gallery</a>
  <span class="sep" style="left:308px"></span>
  <a href="#" style="left:333px">Contact us</a>
</nav>

<aside class="abs panel" style="left:45px;top:393px;width:173px;height:270px"></aside>
<div class="abs ribbon" style="left:37px;top:405px;width:180px">Catagories</div>
<ul class="abs cat-list" style="left:70px;top:448px">
  <li style="top:0">Education</li><li style="top:20px">Healthcare</li><li style="top:41px">Sport</li><li style="top:61px">Migration</li><li style="top:81px">Accommodation</li><li style="top:102px">Tourism</li><li style="top:122px">Arts &amp; Culture</li><li style="top:142px">Case Studies</li><li style="top:163px">Relocation consultant</li><li style="top:183px">Community Services</li>
</ul>

<h2 class="abs biz-title">Business Searches</h2>
<ul class="abs biz-col" style="left:244px;top:445px"><li>CCTV</li><li>Water Jet Pumps</li><li>Movie theaters</li><li>Doctors</li><li>Diesel Generator</li><li>Out Door Advertising</li><li>Bars &amp; Clubs</li><li>Movie theaters</li><li>Bars &amp; Clubs</li><li>Travel Agents</li></ul>
<ul class="abs biz-col" style="left:374px;top:445px"><li>Spa &amp; Salons</li><li>Hospitals</li><li>Furnitures</li><li>Event Planners</li><li>Banks</li><li>Fire Alarm</li><li>Accessories</li><li>Detective Agencies</li><li>Water Jet Pumps</li><li>Out Door Advertising</li></ul>
<ul class="abs biz-col" style="left:511px;top:445px"><li>Jewelry &amp; Watches</li><li>Interior Decorations</li><li>Life Insurance</li><li>House Cleaning</li><li>Doctors</li><li>Home Appliances</li><li>Pest Control</li><li>Security Systems</li><li>Industrial Chemicals</li><li>Packaging Material</li></ul>
<div class="abs biz-rule"></div>

<aside class="abs panel news" style="left:636px;top:393px;width:173px;height:270px">
  <p style="top:54px">Cicero are also reproduced in their exact original form.</p>
  <p style="top:97px">Cicero are also reproduced in their exact original form.</p>
  <p style="top:140px">Cicero are also reproduced in their exact original form.</p>
  <p style="top:184px">Cicero are also reproduced in their exact original form.</p>
  <p style="top:227px">Cicero are also reproduced in their exact original form.</p>
</aside>
<div class="abs ribbon" style="left:628px;top:405px;width:180px">Latest News</div>

<div class="abs alpha">
  <span style="left:61px">0-9</span>
  <span style="left:108px">A</span><span style="left:129px">B</span><span style="left:150px">C</span><span style="left:172px">D</span><span style="left:193px">E</span><span style="left:215px">F</span><span style="left:235px">G</span><span style="left:258px">H</span><span style="left:279px">I</span><span style="left:295px">J</span><span style="left:316px">K</span><span style="left:337px">L</span><span style="left:355px">M</span><span style="left:378px">N</span><span style="left:400px">O</span><span style="left:422px">P</span><span style="left:444px">Q</span><span style="left:466px">R</span><span style="left:487px">S</span><span style="left:509px">T</span><span style="left:530px">U</span><span style="left:552px">V</span><span style="left:572px">W</span><span style="left:597px">X</span><span style="left:618px">Y</span><span style="left:638px">Z</span>
</div>

<section class="abs box-dark reloc" style="left:45px;top:725px;width:173px;height:182px">
  <a href="#" style="top:56px">Work</a><a href="#" style="top:81px">Visit</a><a href="#" style="top:107px">Invest</a><a href="#" style="top:133px">Work</a>
</section>
<div class="abs ribbon light" style="left:38px;top:740px;width:179px">Reloacation Consultant</div>

<section class="abs box-light" style="left:243px;top:729px;width:173px;height:178px"></section>
<div class="abs ribbon dark-sm" style="left:235px;top:740px;width:180px">Newsletter</div>
<div class="abs field" style="left:256px;top:782px">Name</div>
<div class="abs field" style="left:256px;top:817px">Email</div>
<div class="abs btn dark" style="left:332px;top:859px;width:66px">Subscribe</div>

<section class="abs box-dark" style="left:441px;top:725px;width:173px;height:182px"></section>
<div class="abs ribbon light" style="left:434px;top:740px;width:179px">Tell to a friend</div>
<div class="abs field" style="left:458px;top:783px">Name</div>
<div class="abs field" style="left:458px;top:817px">Email</div>
<div class="abs btn light" style="left:545px;top:859px;width:44px">Send</div>

<section class="abs box-light" style="left:639px;top:729px;width:172px;height:178px"></section>
<div class="abs ribbon dark-sm" style="left:631px;top:740px;width:180px">Testimonials</div>
<div class="abs avatar" role="img" aria-label="Reviewer profile photo"></div>
<p class="abs testi-name">Tom Harlow</p>
<p class="abs testi-date">Posted on : 13.11.11</p>
<p class="abs testi-text">Cicero are also reproduced their exact original form, Many desktop publishing packages and web page editors</p>

<div class="abs ad" role="img" aria-label="Advertising banner for a local newspaper programme">
  <div class="ad-ball"></div>
  <span class="ad-head">HOMETOWN FAVOURITE PASTIME</span>
  <span class="ad-brand"><i></i>Paper Club</span>
  <span class="ad-url">www.paperclub.org</span>
</div>

<footer>
  <div class="abs social" style="left:41px;background:#3b5a98" role="img" aria-label="PalNest"></div>
  <div class="abs social" style="left:75px;background:#3fb3e3" role="img" aria-label="Chirpo"></div>
  <div class="abs social" style="left:109px;background:#f07a28" role="img" aria-label="Blogly"></div>
  <div class="abs social" style="left:143px;background:#1f6ea4" role="img" aria-label="LinkUp"></div>
  <div class="abs social" style="left:177px;background:#d8d8d8" role="img" aria-label="Searchly"></div>
  <p class="abs footer-links">About Us | Contact Us | Privacy Policy | Terms of Service | Site map</p>
  <p class="abs copy">© 2011 KemboHub, All Rights Reserved</p>
  <div class="abs roo" role="img" aria-label="Kangaroo standing at the page corner"></div>
</footer>
</body>
</html>
```